Create a packaging design for a new deodorant

New product container label. The jar is 2.75" in diameter and 2.75" high. The (transparent) label size is 1.5" by 8.5" and will wrap nearly fully around the jar when applied. Approximately 3.25" of the label will be devoted to the name and front section of the jar (what I am requesting you to design). Remaining part of the label will include a brief description, directions, general warning, ingredients, manufacturer, distributor, and barcode. The deodorant name is ZOB. It is a clear colorless solution, ecologically friendly, naturally occurring deodorant salt solution. Water based, no alcohol, non-sticky, non-waxy, non-staining, just simple, clean and effective. Nature's way of getting the job done. Label to use transparent green and/or blue colors. Phrases such as " Fresh as a Springtime shower" or "Fresh as an ocean breeze" might be used. The deodorant has a NEW, unique, revolutionary applicator.

Target Market(s)

All adult men and women

Industry/Entity Type

Product

Number of Pages Required

1 page

Requirements
Nice to have
• ZOB
• This is a new deodorant, a simple but elegant solution to an age-old problem.
• Why I Hate Deodorants
• I’ve had my share of problems with deodorants, and with antiperspirants for that matter, too. First off, the last thing I want to do when I step out of the shower is to put some sticky, slimy, or waxy goop on clean skin. I don’t like it when it feels like skin sticks together in skin folds. When I used to use the old stick deodorants, I would periodically scrape the edge of the plastic container against my skin and cause an abrasion that would then be irritated for the next 3 days. This would be particularly true when I got down to the bottom of the stick and the medication surface flattened out in the dispenser. Sometimes the deodorant or antiperspirant itself would cause such abrasions to grow red and angry and force me to stop using it altogether for the next week. Then I’d be hunting (and hurting) for alternatives. So every few months I would spend lots of time in the store looking at all the different brands of deodorants to find something that was a bit different - less caustic, less sticky, less stinky, or in a different dispenser that might work better for me. Roll-on deodorants work for me until they don’t. Half the time I’m trying to hold the bottle upside down and squeezing it so the product comes out. The other half of the time the roller ball gets stuck and I’m trying to get it to turn. What a waste of time. Or if it pours out, I have to spread it all over the place to get it thin enough to dry out. I dispensed with antiperspirants years ago when I had to throw away some of my favorite shirts because of sweat (really antiperspirant chemical) stains. I’ve also seen enough people with hidradenitis (infected sweat glands from using some antiperspirants) to know that some of these products that clog skin pores can be serious skin irritants.
• I’m a Natural Kind of Guy
• Don’t get me wrong. I’m not a tree hugger. I haven’t been out on the high seas in a rowboat maneuvering between a harpooner and a whale. But by the same token I don’t buy 3-step hair treatments. I don’t color my hair either. I don’t lounge around in bubble baths. And I don’t like to use heavy-scented cleansers, shampoos or skin products. I’m just looking for something clean, plain and simple ...something that works, that’s safe and dependable. Maybe even a natural product that has a long track record of safety and effectiveness.
• Just try it.....(There’s nothing more we’ll need to say!!)
• ZOB uses a natural mineral salt, water, and a preservative. Nothing more. ZOB has a unique and patented dispenser. The dispenser was made for the product and made for the job. One swipe application and you’re done! YOU can control the amount of deodorant applied by the sponge applicator. ZOB is WATER-BASED. NO ALCOHOL. NO CHEMICALS. NO IRRITANTS. It dries quickly. No drips like you can get from spray bottles. The applicator doesn’t clog up or stop rolling. And it NEVER stains clothing. It’s just simple...easy...effective. And with a simple product we don’t have to charge a lot of money for it. So it’s inexpensive, too. I know you’re going to like this product.
• Swipe it on.... Odor gone!

```html
<!DOCTYPE html>
<html lang="en">
<head>
<meta charset="utf-8">
<title>ZOB Deodorant – Jar Label</title>
<link rel="stylesheet" href="https://fonts.googleapis.com/css2?family=Open+Sans:wght@400;600;700&display=swap">
<style>
  :root {
    --page: #f4f6f3;
    --label: #ffffff;
    --green: #4f9e2d;
    --green-light: #7cc242;
    --ink: #2c5a1c;
    --muted: #4d7a3b;
    --rule: #e6eee2;
  }
  html, body {
    margin: 0;
    width: 1200px;
    height: 1000px;
    overflow: hidden;
    background: var(--page);
    font-family: "Open Sans", Arial, sans-serif;
  }
  .canvas {
    position: relative;
    width: 1200px;
    height: 1000px;
  }
  .label {
    position: absolute;
    left: 40px;
    top: 290px;
    width: 1120px;
    height: 420px;
    background: var(--label);
    display: grid;
    grid-template-columns: 300px 520px 300px;
    box-shadow: 0 2px 14px rgba(40, 80, 30, 0.12);
  }
  .label__stripe {
    position: absolute;
    left: 0;
    right: 0;
    bottom: 26px;
    height: 7px;
    background: var(--green-light);
  }
  .panel {
    padding: 34px 30px 60px;
    box-sizing: border-box;
    color: var(--muted);
  }
  .panel--side {
    font-size: 17px;
    line-height: 1.65;
  }
  .panel--side p { margin: 0 0 16px; }
  .panel--front {
    display: flex;
    flex-direction: column;
    align-items: center;
    padding-top: 56px;
    border-left: 1px solid var(--rule);
    border-right: 1px solid var(--rule);
  }
  .tagline {
    margin: 0;
    font-size: 22px;
    font-weight: 600;
    letter-spacing: 0.5px;
    color: var(--ink);
  }
  .brand {
    display: flex;
    align-items: center;
    gap: 18px;
    height: 140px;
    margin-top: 8px;
  }
  .brand__dot {
    width: 34px;
    height: 34px;
    border-radius: 50%;
    background: var(--green-light);
    flex: none;
  }
  .brand__name {
    margin: 0;
    font-size: 120px;
    font-weight: 700;
    line-height: 1;
    letter-spacing: 2px;
    color: var(--green);
  }
  .product-type {
    margin: 4px 0 0;
    font-size: 25px;
    font-weight: 600;
    color: var(--ink);
  }
  .claims {
    margin: 22px 0 0;
    font-size: 11px;
    font-weight: 700;
    text-align: center;
    line-height: 1.35;
    color: var(--ink);
  }
  .heading {
    font-weight: 700;
    color: var(--ink);
  }
  .maker {
    font-size: 14px;
    line-height: 1.55;
    margin-top: 22px;
  }
  .maker .heading { font-size: 13px; }
</style>
</head>
<body>
<main class="canvas">
  <section class="label" aria-label="ZOB deodorant jar label, flat">
    <div class="panel panel--side panel--description">
      <p>Clean, clear and simple. A natural mineral salt in water, nothing more.</p>
      <p>Dries fast and never stains your clothing.</p>
      <p>Swipe it on, odor gone.</p>
    </div>

    <div class="panel panel--front">
      <p class="tagline">FRESH AS A SPRING FLOWER</p>
      <div class="brand">
        <span class="brand__dot" aria-hidden="true"></span>
        <h1 class="brand__name">ZOB</h1>
      </div>
      <p class="product-type">DEODORANT</p>
      <p class="claims">WATER BASED NO ALCOHOL NON-STICKY<br>NON-WAXY NON-STAINING</p>
    </div>

    <div class="panel panel--side panel--details">
      <p><span class="heading">INGREDIENTS:</span> Purified water, natural mineral salt, gentle preservative. Nothing more.</p>
      <div class="maker">
        <div class="heading">MANUFACTURED BY:</div>
        <div>ZOB Organics</div>
        <div>P.O. Box 4172</div>
        <div>Meadow Lane</div>
        <div>Greenfield</div>
      </div>
    </div>

    <div class="label__stripe"></div>
  </section>
</main>
</body>
</html>
```